Vela Luxe Gel Top Coat & Base Coat Box Design

We are a wholesale nail and beauty supply company located in the USA. We need an attractive box design for our product, Vela Luxe Gel Top Coat and Base Coat, to boost our sales to retail nail salons in the USA.
Dimension of the box is 11'' wide by 8.25'' long.
Color of the box is black with ingrained pattern (see picture).
Need design for top of box only.

Target Market(s)

Retail Nail Salons in the USA

Industry/Entity Type

Beauty Salon

Colors

Designer to choose colors to be used in the design.

Requirements
Must have
• Luxe Vela Gel Top Coat Base Coat
• Matching Font of our product label (see picture)
Nice to have
• Premium should stand out.
• Line separating design for Top Coat and Base Coat (as they are 2 different products in the same box). Open to all color schemes, but would like to see some in silver.

```html
<!DOCTYPE html>
<html lang="en">
<head>
<meta charset="utf-8">
<title>Vela Luxe Gel Top Coat &amp; Base Coat – Box Lid</title>
<link rel="stylesheet" href="https://fonts.googleapis.com/css2?family=Mulish:wght@300;500&display=swap">
<style>
  :root {
    --page: #ededeb;
    --lid: #262626;
    --lid-edge: #1b1b1b;
    --silver-band: #6c6e73;
    --gold-band: #b8891c;
    --name-silver: #d9dadc;
    --label-white: #f2f2f2;
  }
  * { margin: 0; padding: 0; box-sizing: border-box; }
  html, body {
    width: 1200px;
    height: 900px;
    overflow: hidden;
    background: var(--page);
  }
  .canvas {
    position: relative;
    width: 1200px;
    height: 900px;
  }
  .lid {
    position: absolute;
    left: 120px;
    top: 90px;
    width: 960px;
    height: 720px;
    background: var(--lid);
    box-shadow: inset 0 0 0 2px var(--lid-edge);
    overflow: hidden;
    font-family: "Mulish", sans-serif;
  }
  .band {
    position: absolute;
    left: 0;
    width: 100%;
    display: flex;
    align-items: center;
  }
  .band--top-coat { top: 173px; height: 77px; background: var(--silver-band); }
  .band--base-coat { top: 250px; height: 77px; background: var(--gold-band); }
  .band__label {
    position: absolute;
    left: 630px;
    color: var(--label-white);
    font-weight: 500;
    font-size: 20px;
    line-height: 1;
    letter-spacing: 0.28em;
    white-space: nowrap;
  }
  .brand-name {
    position: absolute;
    left: 70px;
    width: 520px;
    top: 173px;
    height: 154px;
    display: flex;
    align-items: center;
    justify-content: center;
    color: var(--name-silver);
    font-weight: 300;
    font-size: 180px;
    line-height: 1;
    letter-spacing: 0.02em;
    white-space: nowrap;
  }
  .product-line {
    position: absolute;
    left: 0;
    width: 100%;
    top: 540px;
    text-align: center;
    color: var(--label-white);
    font-weight: 500;
    font-size: 26px;
    line-height: 1;
    letter-spacing: 0.7em;
    padding-left: 0.7em;
    white-space: nowrap;
  }
</style>
</head>
<body>
  <main class="canvas">
    <section class="lid" aria-label="Box lid design">
      <div class="band band--top-coat"><span class="band__label">TOP COAT</span></div>
      <div class="band band--base-coat"><span class="band__label">BASE COAT</span></div>
      <h1 class="brand-name">VELA</h1>
      <p class="product-line">LUXE GEL</p>
    </section>
  </main>
</body>
</html>
```